Bluecrest Recovery Massage needs a Website

I'm a Massage Practitioner wanting a website for promotion and bookings with a Blog area and inplementation to my pixelwall page https://www.pixelwall.example/BluecrestRecoveryMassage , my kalviro Booking page http://my.kalviro.example/bookingpage/ab20247d-1234-47c1-bd55-98c7e01a2f3b and my Zentro account to make payments.
The Venues changes from time to time. In October 2015 it will be the Tidewave Multisport Globalfinale in Kona Hawaii

Target Market(s)

Sports People participating in targeted Events

Industry/Entity Type

Massage

Number of Pages Required

5+ page

Font styles to use
Other font styles liked:
• Verdana

Colors
3176b5
5db8de
ec1f27
ffffff

Requirements
Must have
• An About page including which events (in this case Tidewave Multisport Global Finale in Kona, Hawaii in October 2015)
• A page with the Techniques I use
• Inplementation of my Kalviro Booking Page http://my.kalviro.example/bookingpage/ab20247d-1234-47c1-bd55-98c7e01a2f3b
• Implementation of my Pixelwall Page https://www.pixelwall.example/BluecrestRecoveryMassage
Nice to have
• Would be great to have a Blog with Pictures Upload ability
• Tried to upload Pictures but it always says that it is a non supported file type, so contact me to send you those informations. More informations about me to be found on http://wellspringrest.example/about-us/meet-the-team/tad-orlov-haines---massage-therapist.html

```html
<!DOCTYPE html>
<html lang="en">
<head>
<meta charset="utf-8">
<title>Bluecrest Recovery Massage</title>
<link rel="stylesheet" href="https://fonts.googleapis.com/css2?family=Open+Sans:ital,wght@0,400;0,600;1,400&display=swap">
<style>
:root{
  --blue:#3176b5;
  --sky:#5db8de;
  --band:#7ec9ef;
  --red:#ec1f27;
  --white:#ffffff;
  --ink:#444444;
  --muted:#8a8a8a;
  --footer:#f1f1f1;
  --line:#e2e2e2;
}
*{margin:0;padding:0;box-sizing:border-box}
html,body{width:776px;height:1200px;overflow:hidden;background:var(--white)}
body{position:relative;font-family:"Open Sans",Verdana,sans-serif;color:var(--ink)}
.abs{position:absolute}
.topline{left:0;top:0;width:776px;height:2px;background:var(--sky)}
.header{left:0;top:2px;width:776px;height:94px;background:var(--white);box-shadow:0 2px 4px rgba(0,0,0,.12);z-index:2}
.brand{left:62px;top:22px;display:flex;align-items:center;gap:10px}
.brand-dot{width:52px;height:52px;border-radius:50%;background:var(--sky)}
.brand-name{color:var(--red);font-size:13.5px;line-height:16px;font-weight:400;width:110px}
.langs{left:632px;top:16px;display:flex;gap:5px}
.lang{width:17px;text-align:center;font-size:6.5px;color:#bbb}
.lang.on{color:var(--ink)}
.lang i{display:block;width:16px;height:16px;border-radius:50%;margin:0 auto 3px}
.nav{top:61px;font-size:8.5px;color:#555;letter-spacing:.2px}
.nav.on{color:var(--red)}
.band{left:0;top:96px;width:776px;height:326px;background:var(--band)}
.slider{left:64px;top:154px;width:648px;height:334px;background:var(--white);box-shadow:0 8px 10px -6px rgba(0,0,0,.25)}
.slide-photo{left:72px;top:162px;width:632px;height:316px;background:linear-gradient(120deg,#4a4e66 0%,#c9c3b6 40%,#b9443f 62%,#cfcf97 85%,#8d8a55 100%)}
.slide-arrows{left:669px;top:454px;width:35px;height:24px;background:rgba(255,255,255,.75)}
h2{font-weight:400;color:var(--ink);font-size:18px}
.welcome-photo{left:64px;top:558px;width:166px;height:120px;background:linear-gradient(160deg,#7e8a86,#c9c9c0 50%,#5f6a58);border-radius:2px}
.welcome-text{left:249px;top:557px;width:245px;font-size:7.6px;line-height:14.4px;color:var(--muted)}
.btn{display:block;background:var(--blue);color:var(--white);font-size:7.5px;text-align:center;line-height:22px;border-radius:2px;box-shadow:0 1px 2px rgba(0,0,0,.3)}
.quote{left:541px;top:555px;width:172px;font-size:7.8px;line-height:13.2px;font-style:italic;color:var(--blue)}
.quote b{font-style:normal;color:#c8d7e6;font-size:12px;font-weight:600}
.author{left:538px;top:633px;font-size:7px;color:var(--ink)}
.divider{left:64px;top:714px;width:648px;height:1px;background:var(--line)}
.card-photo{top:781px;width:198px;height:116px;border-radius:2px;box-shadow:0 5px 6px -4px rgba(0,0,0,.35)}
.card-title{top:908px;width:198px;font-size:11.2px;line-height:19px;color:var(--red)}
.card-text{width:186px;font-size:7.4px;line-height:14px;color:var(--muted)}
.footer{left:0;top:1021px;width:776px;height:179px;background:var(--footer);border-top:1px solid var(--line)}
.f-head{top:1041px;font-size:10.4px;color:#555}
.feed-thumb{width:45px;height:38px;background:linear-gradient(150deg,#9aa6a8,#d9cfc4 55%,#b44a44)}
.feed-text{left:121px;width:140px;font-size:7.4px;line-height:12px;color:var(--muted)}
.feed-meta{left:121px;font-size:6.8px;color:#aaa}
.feed-meta span{color:var(--blue)}
.links{left:309px;top:1072px;list-style:none;font-size:7.5px;line-height:16px;color:#555}
.links li:first-child{color:var(--red)}
.news-text{left:412px;top:1069px;width:145px;font-size:7.4px;line-height:12px;color:var(--muted)}
.field{left:410px;width:136px;height:26px;background:var(--white);border:1px solid #e0e0e0;font-size:7.2px;color:#666;padding:0 7px;line-height:24px}
.go{left:521px;top:1137px;width:25px;height:25px;background:var(--blue);color:var(--white);font-size:7.5px;text-align:center;line-height:25px}
.social{top:1071px;width:24px;height:24px;border-radius:50%}
.copy{right:64px;top:1123px;text-align:right;font-size:7.4px;line-height:12px;color:#666}
</style>
</head>
<body>
<div class="abs topline"></div>
<header class="abs header">
  <div class="abs brand"><span class="brand-dot"></span><span class="brand-name">Bluecrest Recovery Massage</span></div>
  <div class="abs langs">
    <div class="lang on"><i style="background:#2b3e8f"></i>En</div>
    <div class="lang"><i style="background:linear-gradient(#222 33%,#d11 33% 66%,#f3c300 66%)"></i>Ge</div>
    <div class="lang"><i style="background:linear-gradient(90deg,#1a9a3c 33%,#fff 33% 66%,#d11 66%)"></i>It</div>
    <div class="lang"><i style="background:linear-gradient(90deg,#1f3fa0 33%,#fff 33% 66%,#d11 66%)"></i>Fr</div>
  </div>
  <span class="abs nav on" style="left:411px">HOME</span>
  <span class="abs nav" style="left:466px">SERVICES</span>
  <span class="abs nav" style="left:534px">ABOUT US</span>
  <span class="abs nav" style="left:610px">BLOG</span>
  <span class="abs nav" style="left:662px">CONTACT US</span>
</header>

<div class="abs band"></div>
<div class="abs slider"></div>
<div class="abs slide-photo" role="img" aria-label="Therapist giving a sports massage to an athlete on a treatment table"></div>
<div class="abs slide-arrows">
  <svg width="35" height="24" viewBox="0 0 35 24"><path d="M14 6 L8 12 L14 18 M21 6 L27 12 L21 18" fill="none" stroke="#555" stroke-width="1.2"/></svg>
</div>

<h2 class="abs" style="left:64px;top:517px">Welcome to Massage Practitioner.</h2>
<div class="abs welcome-photo" role="img" aria-label="Athlete celebrating at the finish line of a triathlon"></div>
<p class="abs welcome-text">Tad turned his passion for sport into a passion for helping athletes. As a Massage Therapist he helps athletes to perform optimally and recover faster from training and racing. Tad is trained in Swedish, Remedial &amp; Sports Massage, Active Glide Method (AGM), Deep Layer Fascial Release, Pressure Point Work, Dry Needeling and Lymphatic Drainage.</p>
<a class="abs btn" style="left:249px;top:654px;width:58px">READ MORE</a>

<h2 class="abs" style="left:541px;top:517px">Testimonials</h2>
<p class="abs quote"><b>“</b> Lorem ipsum dolor sit amet, cons ect etur adipiscing elit, sed do eiusmod tempor incididunt ut labore et dolore magna aliqua. Ut enim ad minim veniam, quis nostrud exercitation ullamc.</p>
<div class="abs author">Jhon Smith, City name</div>

<div class="abs divider"></div>
<h2 class="abs" style="left:64px;top:738px">Our Services</h2>

<div class="abs card-photo" style="left:64px;background:linear-gradient(135deg,#8e8a86,#2f6fb2 45%,#d8d6d2)" role="img" aria-label="Therapist stretching an athlete's leg in a treatment room"></div>
<div class="abs card-title" style="left:64px">Sport Deep Tissue Massage</div>
<p class="abs card-text" style="left:64px;top:931px">Lum mleiecneanrit maurillus hertam socatotibus ertas leraeneasmonlusertas lruderugia.</p>
<a class="abs btn" style="left:64px;top:970px;width:60px">READ MORE</a>

<div class="abs card-photo" style="left:289px;background:linear-gradient(135deg,#3b3630,#c49a7c 45%,#6c6a5e)" role="img" aria-label="Hands applying myofascial release to a leg"></div>
<div class="abs card-title" style="left:289px">Myofascial Release</div>
<p class="abs card-text" style="left:289px;top:931px">Lum mleiecneanrit maurillus hertam socatotibus ertas leraeneasmonlusertas lruderugia.</p>
<a class="abs btn" style="left:289px;top:970px;width:60px">READ MORE</a>

<div class="abs card-photo" style="left:514px;background:linear-gradient(135deg,#cfc9c2,#5b5552 50%,#e2dfdb)" role="img" aria-label="Therapist treating an athlete lying on a massage table"></div>
<div class="abs card-title" style="left:514px">Sport Deep Tissue with Active Soft Tissue Work</div>
<p class="abs card-text" style="left:514px;top:945px">Lum mleiecneanrit maurillus hertam socatotibus</p>
<a class="abs btn" style="left:514px;top:970px;width:60px">READ MORE</a>

<footer class="abs footer"></footer>
<div class="abs f-head" style="left:63px">Pixelwall Feeds</div>
<div class="abs f-head" style="left:311px">Links</div>
<div class="abs f-head" style="left:412px">Newsletter</div>
<div class="abs f-head" style="left:594px">Follow Us</div>

<div class="abs feed-thumb" style="left:63px;top:1074px" role="img" aria-label="Post photo of an athlete at an event"></div>
<p class="abs feed-text" style="top:1074px">Lorem ipsum dolor sit amet, conse ctetur adipiscing elit, sed do.</p>
<div class="abs feed-meta" style="top:1104px"><span>June 02 2014</span>&nbsp; 0 Comments</div>
<div class="abs feed-thumb" style="left:63px;top:1127px" role="img" aria-label="Post photo of a group of athletes"></div>
<p class="abs feed-text" style="top:1128px">Lorem ipsum dolor sit amet, conse ctetur adipiscing elit, sed do.</p>
<div class="abs feed-meta" style="top:1158px"><span>June 02 2014</span>&nbsp; 0 Comments</div>

<ul class="abs links">
  <li>Home</li><li>Services</li><li>About Us</li><li>Blog</li><li>Contact Us</li><li>Privacy policy</li>
</ul>

<p class="abs news-text">Lorem ipsum dolor sit amet, conse ctetur adipiscing elit, sed do.</p>
<div class="abs field" style="top:1105px">Name:</div>
<div class="abs field" style="top:1137px">Email</div>
<div class="abs go">GO</div>

<span class="abs social" style="left:595px;background:#1fb6e6"></span>
<span class="abs social" style="left:627px;background:#d42424"></span>
<span class="abs social" style="left:658px;background:#1b73b8"></span>
<span class="abs social" style="left:686px;background:#1a6ea8"></span>

<p class="abs copy">©2015 Massage Practitioner<br>All copyrights reserved.</p>
</body>
</html>
```